DJ Marcus Tevane

I'm looking for a professional but still artsy/progressive design. I come from a hip hop/club DJ background playing a lot of underground music but have switched to doing more corporate parties and weddings recently. I am all about keeping the dancefloor moving and emotionally connecting with the crowd. I'd like a trendy/updated color palette. Something that's clean enough that looks professional but also trendy enough to convey that by the end of the night we'll be sweatily dancing to the latest hits. Some designers/artists I like: Rolo Pemberack, Gavin Struthe, Dorian Fellick, Orbitex 3100, Wade Ipsley.

```html
<!DOCTYPE html>
<html lang="en">
<head>
<meta charset="utf-8">
<title>DJ Marcus Tevane – Business Card</title>
<link rel="stylesheet" href="https://fonts.googleapis.com/css2?family=Oswald:wght@600&family=Open+Sans:wght@400;600;700&display=swap">
<style>
  :root {
    --backdrop: #2b2b2d;
    --card: #121213;
    --card-edge: #1a1a1b;
    --accent: #f07b14;
    --ink-light: #ffffff;
    --ink-muted: #b9b9b9;
    --ink-dim: #8c8c8c;
    --rule: #4a4a4a;
  }
  * { margin: 0; padding: 0; box-sizing: border-box; }
  html, body {
    width: 1200px;
    height: 900px;
    overflow: hidden;
    background: var(--backdrop);
  }
  .stage {
    position: relative;
    width: 1200px;
    height: 900px;
  }
  .card {
    position: absolute;
    width: 525px;
    height: 300px;
    background: linear-gradient(160deg, var(--card-edge), var(--card));
    box-shadow: 0 18px 40px rgba(0, 0, 0, 0.45);
    overflow: hidden;
  }
  .card__band {
    position: absolute;
    left: 0;
    right: 0;
    bottom: 0;
    height: 8px;
    background: var(--accent);
  }

  /* Front */
  .card--front { left: 400px; top: 100px; }
  .brand {
    position: absolute;
    inset: 0 0 8px 0;
    display: flex;
    align-items: center;
    justify-content: center;
    gap: 12px;
  }
  .brand__dot {
    width: 14px;
    height: 14px;
    border-radius: 50%;
    background: var(--accent);
    flex: none;
  }
  .brand__name {
    font-family: "Oswald", sans-serif;
    font-weight: 600;
    font-size: 44px;
    line-height: 1;
    letter-spacing: 0.5px;
    text-transform: uppercase;
    color: var(--ink-light);
    white-space: nowrap;
  }

  /* Back */
  .card--back { left: 275px; top: 470px; }
  .holder {
    position: absolute;
    left: 95px;
    top: 88px;
    width: 175px;
    text-align: right;
  }
  .holder__name {
    font-family: "Open Sans", sans-serif;
    font-weight: 700;
    font-size: 17px;
    line-height: 22px;
    letter-spacing: 0.5px;
    color: var(--accent);
    text-transform: uppercase;
    white-space: nowrap;
  }
  .holder__role {
    font-family: "Open Sans", sans-serif;
    font-size: 14px;
    line-height: 18px;
    color: var(--ink-dim);
    white-space: nowrap;
  }
  .divider {
    position: absolute;
    left: 290px;
    top: 84px;
    width: 1px;
    height: 70px;
    background: var(--rule);
  }
  .contacts {
    position: absolute;
    left: 306px;
    top: 84px;
    list-style: none;
    font-family: "Open Sans", sans-serif;
    font-size: 14px;
    line-height: 17.5px;
    color: var(--ink-muted);
    white-space: nowrap;
  }
  .contacts li { display: flex; align-items: center; gap: 8px; }
  .contacts svg { width: 11px; height: 11px; fill: var(--accent); flex: none; }
  .address {
    position: absolute;
    left: 0;
    right: 0;
    top: 196px;
    text-align: center;
    font-family: "Open Sans", sans-serif;
    font-size: 14px;
    color: var(--ink-dim);
    white-space: nowrap;
  }
</style>
</head>
<body>
<main class="stage">

  <section class="card card--front" aria-label="Card front">
    <div class="brand">
      <span class="brand__dot"></span>
      <span class="brand__name">DJ Marcus Tevane</span>
    </div>
    <div class="card__band"></div>
  </section>

  <section class="card card--back" aria-label="Card back">
    <div class="holder">
      <p class="holder__name">Lena Darrow</p>
      <p class="holder__role">Managing Director</p>
    </div>
    <div class="divider"></div>
    <ul class="contacts">
      <li>
        <svg viewBox="0 0 12 12" aria-hidden="true"><path d="M1 3c0-1 1-2 2-2h6c1 0 2 1 2 2v1H8V3H4v1H1z M2 5h8l1 5H1z M5 6.5h2v2H5z"/></svg>
        044-555 210 384
      </li>
      <li>
        <svg viewBox="0 0 12 12" aria-hidden="true"><path d="M3.5 0h5a1 1 0 0 1 1 1v10a1 1 0 0 1-1 1h-5a1 1 0 0 1-1-1V1a1 1 0 0 1 1-1zM4 1.5v7.5h4V1.5zM6 10a.6.6 0 1 0 0 1.2A.6.6 0 0 0 6 10z"/></svg>
        044-555 210 397
      </li>
      <li>
        <svg viewBox="0 0 12 12" aria-hidden="true"><path d="M0 2h12v8H0zM1 3l5 4 5-4v-.2H1z"/></svg>
        info@tevanesound.com
      </li>
      <li>
        <svg viewBox="0 0 12 12" aria-hidden="true"><circle cx="6" cy="6" r="5.5"/></svg>
        www.tevanesound.com
      </li>
    </ul>
    <p class="address">48, Larkfield Row Brenton Vale Norvania, 204871.</p>
    <div class="card__band"></div>
  </section>

</main>
</body>
</html>
```